Cover design for a writing pad and lecture pad

I need a cover design for writing pad and lecture pad for school students target age from 11 years old to 18 years old. The cover design could be any things, we are open to any idea and design, attached a sample of my current design for reference.

Target Market(s)

Target student age of 11 to 18

Industry/Entity Type

School

```html
<!DOCTYPE html>
<html lang="en">
<head>
<meta charset="utf-8">
<title>NOTIVA A5 Lecture Pad Cover</title>
<link href="https://fonts.googleapis.com/css2?family=Archivo:wght@700;800;900&display=swap" rel="stylesheet">
<style>
  :root {
    --page: #ffffff;
    --cover-mint: #c6d9d1;
    --cover-grey: #b3c3c9;
    --cover-warm: #cfd6d3;
    --tag-black: #111111;
    --bubble-black: #0b0b0b;
    --sticker-edge: #ffffff;
    --ink-white: #ffffff;
    --green: #4fb22c;
    --yellow: #f2c81c;
    --orange: #ef6a24;
    --red: #d5262a;
    --blue: #2f7fd0;
    --sky: #58a9e6;
    --purple: #8c4fb0;
    --peach: #f2c392;
    --grey-metal: #6f6f6f;
    --leaf: #4c9a3a;
  }
  * { margin: 0; padding: 0; box-sizing: border-box; }
  html, body {
    width: 900px; height: 1200px; overflow: hidden;
    background: var(--page);
    font-family: "Archivo", Arial, sans-serif;
  }
  .canvas { position: relative; width: 900px; height: 1200px; }
  .pad-cover {
    position: absolute; left: 170px; top: 202px;
    width: 558px; height: 783px; overflow: hidden;
  }
  .pad-cover svg { display: block; }
  .tag-stroke { fill: none; stroke: var(--tag-black); stroke-width: 9; stroke-linecap: round; opacity: .85; }
  .sticker { stroke: var(--sticker-edge); stroke-width: 5; }
  .cloud { fill: var(--bubble-black); stroke: var(--sticker-edge); stroke-width: 6; }
  .bubble-text {
    font-family: "Archivo", Arial, sans-serif;
    fill: var(--ink-white);
    text-anchor: middle;
  }
  .brand-name { font-weight: 900; font-size: 32px; letter-spacing: 1px; }
  .mind-line { font-weight: 800; font-size: 12.5px; }
  .calm-small { font-weight: 800; font-size: 8.5px; }
  .calm-big { font-weight: 900; font-size: 17px; }
  .size-big { font-weight: 900; font-size: 26px; }
  .size-mid { font-weight: 800; font-size: 15px; }
  .size-small { font-weight: 800; font-size: 7.5px; }
</style>
</head>
<body>
<div class="canvas">
  <div class="pad-cover">
    <svg width="558" height="783" viewBox="0 0 558 783">
      <defs>
        <linearGradient id="cover-tones" x1="0" y1="0" x2="1" y2="1">
          <stop offset="0" stop-color="var(--cover-mint)"/>
          <stop offset="0.5" stop-color="var(--cover-grey)"/>
          <stop offset="1" stop-color="var(--cover-warm)"/>
        </linearGradient>
      </defs>

      <rect class="cover-ground" width="558" height="783" fill="url(#cover-tones)"/>

      <!-- background street strokes -->
      <g class="street-strokes">
        <path class="tag-stroke" d="M10 20 q80 40 140 0 t160 30"/>
        <path class="tag-stroke" d="M120 110 q60 -40 110 10 t80 60"/>
        <path class="tag-stroke" d="M260 260 q50 60 120 20 t140 40"/>
        <path class="tag-stroke" d="M60 450 q70 50 150 10 t120 60"/>
        <path class="tag-stroke" d="M200 560 q60 -30 120 20 t130 -10"/>
        <path class="tag-stroke" d="M20 640 q90 30 150 -20"/>
        <path class="tag-stroke" d="M380 520 q60 40 170 20"/>
      </g>

      <!-- sticker placeholders -->
      <g class="sticker-set">
        <rect class="sticker" x="20" y="33" width="110" height="75" rx="30" fill="var(--green)" role="img" aria-label="Green graffiti SHARE lettering sticker"/>
        <ellipse class="sticker" cx="205" cy="38" rx="24" ry="26" fill="var(--tag-black)" role="img" aria-label="Black cartoon hand gesture sticker"/>
        <ellipse class="sticker" cx="260" cy="60" rx="34" ry="38" fill="var(--blue)" role="img" aria-label="Blue strawberry sticker"/>
        <ellipse class="sticker" cx="457" cy="113" rx="32" ry="24" fill="var(--red)" role="img" aria-label="Red lips sticker"/>
        <ellipse class="sticker" cx="530" cy="96" rx="32" ry="34" fill="var(--orange)" role="img" aria-label="Orange megaphone sticker"/>
        <rect class="sticker" x="390" y="112" width="130" height="60" rx="26" fill="var(--leaf)" role="img" aria-label="Green graffiti POST lettering sticker"/>
        <rect class="sticker" x="20" y="140" width="108" height="76" rx="30" fill="var(--yellow)" role="img" aria-label="Yellow speech bubble sticker"/>
        <rect class="sticker" x="318" y="118" width="66" height="80" rx="22" fill="var(--grey-metal)" role="img" aria-label="Hand holding a phone sticker"/>
        <rect class="sticker" x="425" y="180" width="105" height="72" rx="28" fill="var(--yellow)" role="img" aria-label="Yellow graffiti SHARE lettering sticker"/>
        <ellipse class="sticker" cx="77" cy="270" rx="42" ry="26" fill="var(--red)" role="img" aria-label="Red lips sticker"/>
        <rect class="sticker" x="238" y="220" width="90" height="82" rx="30" fill="var(--peach)" role="img" aria-label="Cartoon cat sticker"/>
        <rect class="sticker" x="346" y="210" width="68" height="88" rx="28" fill="var(--sky)" role="img" aria-label="Blue cartoon creature sticker"/>
        <rect class="sticker" x="-10" y="228" width="38" height="92" rx="16" fill="var(--leaf)" role="img" aria-label="Green broccoli character sticker"/>
        <rect class="sticker" x="530" y="218" width="40" height="90" rx="18" fill="var(--ink-white)" role="img" aria-label="White camera lens sticker"/>
        <rect class="sticker" x="426" y="268" width="84" height="108" rx="34" fill="var(--purple)" role="img" aria-label="Purple map pin sticker"/>
        <rect class="sticker" x="190" y="298" width="112" height="94" rx="34" fill="var(--orange)" role="img" aria-label="Orange graffiti SHARE lettering sticker"/>
        <rect class="sticker" x="320" y="308" width="98" height="98" rx="34" fill="var(--sky)" role="img" aria-label="Blue bird sticker"/>
        <rect class="sticker" x="-10" y="345" width="68" height="92" rx="24" fill="var(--tag-black)" role="img" aria-label="Black and white cartoon hand sticker"/>
        <ellipse class="sticker" cx="274" cy="428" rx="24" ry="30" fill="var(--tag-black)" role="img" aria-label="Rock hand gesture sticker"/>
        <ellipse class="sticker" cx="146" cy="468" rx="44" ry="58" fill="var(--red)" role="img" aria-label="Red round bomb sticker"/>
        <ellipse class="sticker" cx="350" cy="478" rx="40" ry="50" fill="var(--red)" role="img" aria-label="Red strawberry sticker"/>
        <ellipse class="sticker" cx="472" cy="458" rx="72" ry="68" fill="var(--tag-black)" role="img" aria-label="Large black and white eye camera sticker"/>
        <rect class="sticker" x="-6" y="440" width="94" height="106" rx="32" fill="var(--sky)" role="img" aria-label="Blue bird sticker"/>
        <rect class="sticker" x="176" y="490" width="84" height="66" rx="28" fill="var(--sky)" role="img" aria-label="Blue play button sticker"/>
        <rect class="sticker" x="45" y="528" width="95" height="98" rx="34" fill="var(--orange)" role="img" aria-label="Orange megaphone sticker"/>
        <rect class="sticker" x="160" y="585" width="60" height="62" rx="22" fill="var(--grey-metal)" role="img" aria-label="Hand holding a phone sticker"/>
        <rect class="sticker" x="240" y="556" width="118" height="90" rx="36" fill="var(--ink-white)" role="img" aria-label="Red cartoon car in a cloud sticker"/>
        <rect class="sticker" x="370" y="545" width="104" height="72" rx="28" fill="var(--purple)" role="img" aria-label="Purple graffiti SHARE lettering sticker"/>
        <rect class="sticker" x="486" y="608" width="56" height="70" rx="24" fill="var(--leaf)" role="img" aria-label="Green broccoli character sticker"/>
        <rect class="sticker" x="25" y="668" width="135" height="88" rx="34" fill="var(--blue)" role="img" aria-label="Blue graffiti SHARE lettering sticker"/>
        <ellipse class="sticker" cx="258" cy="730" rx="34" ry="46" fill="var(--blue)" role="img" aria-label="Blue strawberry sticker"/>
        <ellipse class="sticker" cx="530" cy="748" rx="36" ry="34" fill="var(--orange)" role="img" aria-label="Orange megaphone sticker"/>
      </g>

      <!-- brand cloud -->
      <g class="brand-cloud">
        <path class="cloud" d="M330 20 a30 30 0 0 1 45-18 a35 35 0 0 1 60 0 a30 30 0 0 1 45 25 a28 28 0 0 1 0 45 a30 30 0 0 1-45 22 a35 35 0 0 1-60 0 a30 30 0 0 1-45-22 a28 28 0 0 1 0-52 z"/>
        <text class="bubble-text brand-name" x="405" y="58">NOTIVA</text>
      </g>

      <!-- thought bubble -->
      <g class="mind-bubble">
        <path class="cloud" d="M155 150 a32 32 0 0 1 45-28 a32 32 0 0 1 55 5 a30 30 0 0 1 20 50 a30 30 0 0 1-5 55 a32 32 0 0 1-55 25 a32 32 0 0 1-55-10 a30 30 0 0 1-25-50 a30 30 0 0 1 20-47z"/>
        <text class="bubble-text mind-line" x="215" y="200">WHAT'S</text>
        <text class="bubble-text mind-line" x="215" y="217">ON YOUR</text>
        <text class="bubble-text mind-line" x="215" y="234">MIND?</text>
      </g>

      <!-- calm bubble -->
      <g class="calm-bubble">
        <path class="cloud" d="M75 330 a28 28 0 0 1 45-18 a28 28 0 0 1 45 10 a25 25 0 0 1 10 40 a28 28 0 0 1-25 45 a30 30 0 0 1-45 5 a28 28 0 0 1-45-25 a25 25 0 0 1 15-57z"/>
        <text class="bubble-text calm-small" x="112" y="348">KEEP CALM</text>
        <text class="bubble-text calm-small" x="118" y="358">AND TAKE IT</text>
        <text class="bubble-text calm-big" x="112" y="378">EASY</text>
      </g>

      <!-- pad size bubble -->
      <g class="size-bubble">
        <path class="cloud" d="M345 640 a35 35 0 0 1 55-20 a35 35 0 0 1 60 12 a30 30 0 0 1 25 50 a32 32 0 0 1-25 55 a35 35 0 0 1-60 10 a35 35 0 0 1-55-15 a30 30 0 0 1-20-45 a30 30 0 0 1 20-47z"/>
        <text class="bubble-text size-big" x="385" y="667">A5</text>
        <text class="bubble-text size-mid" x="400" y="691">Lecture pad</text>
        <text class="bubble-text size-mid" x="400" y="710">210x148 mm</text>
        <text class="bubble-text size-small" x="400" y="722">70gsm, 70 sheets</text>
      </g>
    </svg>
  </div>
</div>
</body>
</html>
```